New Business Card Design Project

We require a business card design for Zelvaquin, a newly established Indian company.
Our focus is on the development, manufacturing, and export of a diverse array of pharmaceutical products on a global scale. The card should convey a professional appearance, as our primary markets are in Africa, China, and Southeast Asian nations.
We envision a two-sided business card, with the reverse side dedicated to a logo set against a solid color or an elegantly designed pattern. The corners should be rounded. We would appreciate seeing both horizontal and vertical design options. We trust the designer to utilize their expertise in creating this design.

The content for the business card is included in the attached Word file.

Target Market(s)

Our primary markets are in Africa, China, and Southeast Asian, Latin America, Maldives, Sri Lanka

Industry/Entity Type

Pharmaceutical Manufacturing and Export

Contact Information for Business Card

Colors

Designer to choose colors to be used in the design.

Requirements
Must have
• The reverse side of the business card features solely the logo along with the tagline, "Remedies of Life."
Should not have
• The logo should not exceed two instances, encompassing both the front and back sides of the card.

```html
<!DOCTYPE html>
<html lang="en">
<head>
<meta charset="utf-8">
<title>Zelvaquin Business Card</title>
<link href="https://fonts.googleapis.com/css2?family=Roboto:wght@400;500;700&family=Roboto+Condensed:wght@400&display=swap" rel="stylesheet">
<style>
  :root {
    --brand-blue: #2fb5ea;
    --accent-red: #ee3a45;
    --text-dark: #454545;
    --card-bg: #ffffff;
    --card-border: #cbe6f3;
    --page-bg: #ffffff;
  }
  html, body {
    margin: 0;
    padding: 0;
    width: 1200px;
    height: 705px;
    overflow: hidden;
    background: var(--page-bg);
  }
  .card {
    position: relative;
    width: 1196px;
    height: 701px;
    margin: 2px;
    box-sizing: border-box;
    border: 3px solid var(--card-border);
    border-radius: 26px;
    background: var(--card-bg);
    font-family: "Roboto", Arial, sans-serif;
    overflow: hidden;
  }
  .brand-name {
    position: absolute;
    left: 0;
    width: 560px;
    top: 410px;
    margin: 0;
    text-align: center;
    font-size: 62px;
    font-weight: 500;
    color: var(--brand-blue);
    line-height: 1;
  }
  .divider {
    position: absolute;
    left: 526px;
    top: 148px;
    width: 3px;
    height: 466px;
    background: var(--accent-red);
  }
  .details {
    position: absolute;
    left: 614px;
    top: 145px;
  }
  .person-name {
    margin: 0;
    font-size: 38px;
    font-weight: 500;
    color: var(--brand-blue);
    line-height: 40px;
  }
  .person-title {
    margin: 9px 0 0;
    font-size: 23px;
    font-weight: 400;
    color: var(--brand-blue);
    line-height: 24px;
  }
  .contact {
    margin: 42px 0 0;
    font-size: 31px;
    font-weight: 500;
    color: var(--accent-red);
    line-height: 40px;
  }
  .contact .label {
    display: inline-block;
    width: 58px;
    font-weight: 700;
  }
  .address {
    margin: 58px 0 0;
    font-family: "Roboto Condensed", "Arial Narrow", sans-serif;
    font-size: 34px;
    color: var(--text-dark);
    line-height: 45px;
    font-style: normal;
  }
  .website {
    margin: 28px 0 0;
    font-size: 30px;
    font-weight: 700;
    color: var(--accent-red);
    line-height: 30px;
  }
</style>
</head>
<body>
  <div class="card">
    <p class="brand-name">Zelvaquin</p>
    <div class="divider"></div>
    <div class="details">
      <h1 class="person-name">Ravin K. Solanke</h1>
      <p class="person-title">CEO Zelvaquin</p>
      <p class="contact">
        <span class="label">e.</span>rsolanke@zelvaquin.com<br>
        <span class="label">m.</span>+919830571642
      </p>
      <address class="address">
        Plot No.14, Sundar Colony,<br>
        Ashok Marg, Nandpur,<br>
        Pin Code: 440918, Maharashtra, India
      </address>
      <p class="website">www.zelvaquin.com</p>
    </div>
  </div>
</body>
</html>
```